Investment firm needs refreshed corporate powerpoint slides design

We need a new and refreshed powerpoint template for our corporate investment deck. We are a technology private equity group that primarily invests in fast growing software companies and we would like to reflect that in a modern and light blue / transparant / white powerpoint and fonts template. I have also attached our old investor deck as a guideline and also check out our website to get an idea of what we do and what type of companies we invested in. Please note that our website is old and so our presentation should be a refreshed "2017" modern design, not a copy / paste of our website design and graphics.
Updates

Target Market(s)

Investors such as high net worth individuals, pension funds, banks, financial advisors

Industry/Entity Type

Investment

Colors
33a6d7
85cae6
cfeae6
edf8f6
ffffff
fff3d1
86cfc6

Requirements
Must have
• We let you be creative, we trust you have seen more investment presentations before.
Nice to have
• Pre-built models, flow charts, graphs, charts, etc.
Should not have
• Fancy or edgy images, this has to be a modern, fresh and trustworthy looking powerpoint template. No stock images, if you do use stock images for background purposes please be creative! :-)

```html
<!DOCTYPE html>
<html lang="en">
<head>
<meta charset="utf-8">
<title>Arvelle — Corporate Investment Deck Template</title>
<link href="https://fonts.googleapis.com/css2?family=Raleway:wght@400;600;700;800&family=Open+Sans:wght@400;600&display=swap" rel="stylesheet">
<style>
:root{
  --navy:#1b3657;
  --deep:#0e2442;
  --blue:#33a6d7;
  --sky:#85cae6;
  --mint:#cfeae6;
  --ice:#edf8f6;
  --teal:#86cfc6;
  --steel:#5f97b5;
  --slate:#7fa9c0;
  --gray:#8a96a3;
  --pale:#c8d2da;
  --line:#dfe6eb;
  --ink:#3c4650;
  --page:#eef1f3;
  --land:#cfd6dc;
}
*{box-sizing:border-box;margin:0;padding:0}
html,body{width:1200px;height:3331px;overflow:hidden;background:var(--page)}
body{font-family:"Open Sans",sans-serif;color:var(--ink)}
.deck{display:grid;grid-template-columns:repeat(3,389px);grid-auto-rows:215px;gap:7px 11px;padding:4px 5px;width:1200px;height:3331px}
.slide{position:relative;overflow:hidden;background:#fff}
.slide.std::after{content:"";position:absolute;left:0;right:0;top:30px;height:1px;background:var(--line)}
.slide.std::before{content:"";position:absolute;right:0;bottom:0;border-style:solid;border-width:0 0 12px 12px;border-color:transparent transparent var(--pale) transparent}
.abs{position:absolute}
.title{position:absolute;left:14px;top:9px;font:700 13px/1.1 "Raleway",sans-serif;color:var(--navy)}
.brand{position:absolute;right:12px;top:8px;font:700 13px/1.1 "Raleway",sans-serif;color:var(--navy)}
.brand::before{content:"";display:inline-block;width:5px;height:5px;background:var(--sky);margin-right:4px;vertical-align:middle}
.brand.light{color:#fff}
.brand.big{font-size:30px}
.brand.huge{font-size:40px}
.lead{font:700 8px/1.35 "Raleway",sans-serif;color:var(--navy)}
.h{font:700 6.5px/1.3 "Raleway",sans-serif;color:var(--navy)}
.h.w,.p.w,.lead.w{color:#fff}
.p{font:400 5px/1.55 "Open Sans",sans-serif;color:var(--gray)}
.photo{position:absolute}
.ph-ice{background:radial-gradient(circle at 25% 30%,rgba(255,255,255,.7),transparent 45%),radial-gradient(circle at 80% 75%,rgba(95,151,181,.45),transparent 50%),linear-gradient(135deg,#e3f1f6,#a8cfe0 60%,#7fb3cd)}
.ph-sky{background:radial-gradient(circle at 70% 35%,rgba(255,255,255,.45),transparent 40%),radial-gradient(circle at 20% 80%,rgba(27,54,87,.35),transparent 55%),linear-gradient(135deg,#a6d2e4,#6aa6c6 55%,#4a88ad)}
.ph-teal{background:radial-gradient(circle at 75% 40%,rgba(237,248,246,.5),transparent 45%),radial-gradient(circle at 15% 85%,rgba(95,151,181,.4),transparent 55%),linear-gradient(135deg,#a7d6da,#74b3c4 60%,#5b9bb3)}
.ph-dark{background:radial-gradient(circle at 65% 45%,rgba(133,202,230,.55),transparent 40%),radial-gradient(circle at 20% 20%,rgba(51,166,215,.3),transparent 45%),linear-gradient(135deg,#0a1d38,#1f4f83 55%,#3a7fb8)}
.ph-green{background:radial-gradient(circle at 60% 40%,rgba(80,200,120,.35),transparent 45%),linear-gradient(135deg,#04110b,#0e3a22 55%,#1f6b3d)}
.ph-map{background:radial-gradient(ellipse at 30% 40%,#c3ccd3,transparent 35%),radial-gradient(ellipse at 72% 55%,#c3ccd3,transparent 38%),linear-gradient(135deg,#e4e9ed,#d3dae0)}
.pin{position:absolute;width:7px;height:7px;border-radius:50%;background:var(--blue);box-shadow:0 0 0 3px rgba(51,166,215,.25)}
.pin.teal{background:var(--teal);box-shadow:0 0 0 3px rgba(134,207,198,.3)}
.ic{position:absolute;width:12px;height:12px;border-radius:50%;background:var(--steel)}
.ic::after{content:"";position:absolute;left:4px;top:4px;width:4px;height:4px;border-radius:50%;background:#fff}
.ic.sq{border-radius:2px}
.ic.teal{background:var(--teal)}
.ic.sky{background:var(--sky)}
.panel{position:absolute}
.bar{position:absolute;height:16px}
.num{font:800 11px/16px "Raleway",sans-serif;color:#fff;text-align:center}
.big-type{font:700 11px/1.35 "Raleway",sans-serif;color:#fff}
.cap{font:600 7px/1 "Raleway",sans-serif;letter-spacing:1.5px;color:#fff}
.badge{position:absolute;background:#3a3f45}
</style>
</head>
<body>
<main class="deck">

<!-- 1 cover -->
<section class="slide">
  <div class="photo ph-ice" style="inset:0" role="img" aria-label="Light blue abstract technology background"></div>
  <div class="brand huge" style="left:34px;top:84px;right:auto">Arvelle</div>
</section>

<!-- 2 title with chevrons -->
<section class="slide">
  <div class="photo ph-dark" style="left:0;top:0;width:240px;height:120px;clip-path:polygon(0 0,100% 0,70% 100%,0 100%)" role="img" aria-label="Dark blue city and data imagery in chevron shapes"></div>
  <div class="panel" style="left:178px;top:22px;width:56px;height:56px;background:var(--steel);transform:rotate(45deg)"></div>
  <div class="brand light" style="left:180px;top:43px;right:auto">Arvelle</div>
  <div class="abs" style="left:0;right:0;top:150px;text-align:center;font:700 15px 'Raleway',sans-serif;color:var(--navy)">Your Title Goes Here</div>
  <div class="p abs" style="left:0;right:0;top:170px;text-align:center">Your subtitle here</div>
</section>

<!-- 3 title light -->
<section class="slide">
  <div class="photo ph-ice" style="inset:0" role="img" aria-label="Soft blue binary data background"></div>
  <div class="brand light big" style="left:150px;top:30px;right:auto">Arvelle</div>
  <div class="abs" style="left:150px;top:74px;font:700 13px 'Raleway',sans-serif;color:var(--navy)">Your Title Goes Here</div>
  <div class="p abs" style="left:180px;top:92px;color:var(--navy)">Your subtitle here</div>
</section>

<!-- 4 agenda -->
<section class="slide std">
  <div class="title">Our Agenda</div><div class="brand">Arvelle</div>
  <div class="ic sq sky" style="left:28px;top:50px"></div><div class="abs" style="left:46px;top:49px;width:120px"><div class="h">Agenda One</div><div class="p">Short note on this part of the meeting plan.</div></div>
  <div class="ic sq sky" style="left:28px;top:95px"></div><div class="abs" style="left:46px;top:94px;width:120px"><div class="h">Agenda Two</div><div class="p">Short note on this part of the meeting plan.</div></div>
  <div class="ic sq sky" style="left:28px;top:140px"></div><div class="abs" style="left:46px;top:139px;width:120px"><div class="h">Agenda Three</div><div class="p">Short note on this part of the meeting plan.</div></div>
  <div class="ic sq sky" style="left:205px;top:50px"></div><div class="abs" style="left:223px;top:49px;width:120px"><div class="h">Agenda Four</div><div class="p">Short note on this part of the meeting plan.</div></div>
  <div class="ic sq sky" style="left:205px;top:95px"></div><div class="abs" style="left:223px;top:94px;width:120px"><div class="h">Agenda Five</div><div class="p">Short note on this part of the meeting plan.</div></div>
  <div class="ic sq sky" style="left:205px;top:140px"></div><div class="abs" style="left:223px;top:139px;width:120px"><div class="h">Agenda Six</div><div class="p">Short note on this part of the meeting plan.</div></div>
</section>

<!-- 5 about collage -->
<section class="slide">
  <div class="photo ph-dark" style="left:0;top:0;width:389px;height:110px" role="img" aria-label="Dark blue world map and city imagery"></div>
  <div class="p w abs" style="left:222px;top:14px;width:155px;font-size:6px">Arvelle is an experienced growth equity investor with a track record of backing global market leaders and delivering top returns.</div>
  <div class="panel" style="left:0;top:110px;width:200px;height:105px;background:var(--teal)"></div>
  <div class="p w abs" style="left:14px;top:140px;width:170px;font-size:6px">Known brands in Europe and North America: businesses with real customers and strong revenue growth.</div>
  <div class="photo ph-dark" style="left:200px;top:110px;width:189px;height:105px;opacity:.85" role="img" aria-label="Data streams over dark blue background"></div>
</section>

<!-- 6 statement -->
<section class="slide">
  <div class="photo ph-teal" style="inset:0" role="img" aria-label="Teal background with faint digital figure"></div>
  <div class="big-type abs" style="left:18px;top:36px;width:210px">Arvelle Is A Growth Equity Investor. Our Investment Approach Reflects The Needs And Opportunities Of Founder-led Companies.</div>
</section>

<!-- 7 quote -->
<section class="slide">
  <div class="photo ph-sky" style="inset:0" role="img" aria-label="Portrait photo with soft blue overlay"></div>
  <div class="abs" style="left:180px;top:54px;width:28px;height:28px;border-radius:50%;background:#fff;text-align:center;font:800 18px/34px 'Raleway',sans-serif;color:var(--steel)">“</div>
  <div class="abs" style="left:80px;top:94px;width:230px;text-align:center;font:600 8px/1.4 'Raleway',sans-serif;color:#fff">Coming together is a beginning. Keeping together is progress. Working together is success.</div>
  <div class="p w abs" style="left:0;right:0;top:130px;text-align:center">Founder Name</div>
</section>

<!-- 8 vision mission -->
<section class="slide std">
  <div class="title">Our Vision &amp; Mission</div><div class="brand">Arvelle</div>
  <div class="panel" style="left:14px;top:42px;width:180px;height:158px;background:var(--steel)"></div>
  <div class="abs" style="left:26px;top:56px;width:156px"><div class="h w">Our Vision:</div><div class="lead w">Go to the Next Level Without limit is the goal</div><div class="p w" style="margin-top:6px">Short statement on where the firm is heading and the companies it wants to back in the years ahead.</div></div>
  <div class="panel" style="left:196px;top:42px;width:180px;height:158px;background:var(--slate)"></div>
  <div class="abs" style="left:208px;top:56px;width:156px"><div class="h w">Our Mission:</div>
    <div class="p w" style="margin-top:6px">● Back founders with capital and care.</div>
    <div class="p w" style="margin-top:6px">● Help teams scale into new markets.</div>
    <div class="p w" style="margin-top:6px">● Build value that lasts for investors.</div>
  </div>
</section>

<!-- 9 previous work -->
<section class="slide">
  <div class="badge" style="left:28px;top:30px;width:48px;height:14px"></div>
  <div class="badge" style="left:110px;top:24px;width:24px;height:24px;border-radius:50%"></div>
  <div class="badge" style="left:180px;top:28px;width:56px;height:16px"></div>
  <div class="badge" style="left:300px;top:30px;width:48px;height:12px"></div>
  <div class="badge" style="left:28px;top:84px;width:24px;height:24px;border-radius:50%"></div>
  <div class="panel" style="left:130px;top:74px;width:164px;height:46px;background:var(--sky)"></div>
  <div class="abs" style="left:130px;top:90px;width:164px;text-align:center;font:700 10px 'Raleway',sans-serif;color:#fff">Our Previous work</div>
  <div class="badge" style="left:320px;top:84px;width:26px;height:26px"></div>
  <div class="badge" style="left:28px;top:160px;width:44px;height:14px"></div>
  <div class="badge" style="left:110px;top:156px;width:24px;height:24px;border-radius:50%"></div>
  <div class="badge" style="left:180px;top:160px;width:56px;height:14px"></div>
  <div class="badge" style="left:300px;top:156px;width:24px;height:24px;border-radius:50%"></div>
</section>

<!-- 10 text + photo -->
<section class="slide std">
  <div class="title">Your Title Goes Here</div><div class="brand">Arvelle</div>
  <div class="abs" style="left:14px;top:44px;width:170px"><div class="lead">This is place for your header text. Insert your text here, just replace this text with your own text.</div><div class="p" style="margin-top:8px">Short body copy describing the point of this slide in a few plain lines for the reader.</div><div class="p" style="margin-top:6px">A second short paragraph that adds one more supporting detail.</div></div>
  <div class="photo ph-sky" style="left:200px;top:34px;width:178px;height:168px" role="img" aria-label="Portrait with blue digital mosaic overlay"></div>
</section>

<!-- 11 portfolio -->
<section class="slide std">
  <div class="title">Portfolio Area</div><div class="brand">Arvelle</div>
  <div class="h abs" style="left:14px;top:40px">Heading Goes Here</div>
  <div class="p abs" style="left:14px;top:50px;width:150px">Short line about the portfolio shown on this slide.</div>
  <div class="ic" style="left:20px;top:80px"></div><div class="abs" style="left:38px;top:80px"><div class="h">Your Text Here</div><div class="p">Brief detail</div></div>
  <div class="ic" style="left:20px;top:108px"></div><div class="abs" style="left:38px;top:108px"><div class="h">Your Text Here</div><div class="p">Brief detail</div></div>
  <div class="ic" style="left:20px;top:136px"></div><div class="abs" style="left:38px;top:136px"><div class="h">Your Text Here</div><div class="p">Brief detail</div></div>
  <div class="ic" style="left:20px;top:164px"></div><div class="abs" style="left:38px;top:164px"><div class="h">Your Text Here</div><div class="p">Brief detail</div></div>
  <div class="photo ph-dark" style="left:180px;top:40px;width:96px;height:78px" role="img" aria-label="Abstract data imagery"></div>
  <div class="photo ph-ice" style="left:280px;top:40px;width:96px;height:78px" role="img" aria-label="Office building imagery"></div>
  <div class="photo ph-sky" style="left:180px;top:122px;width:96px;height:78px" role="img" aria-label="Technology imagery"></div>
  <div class="photo ph-dark" style="left:280px;top:122px;width:96px;height:78px;filter:hue-rotate(-10deg)" role="img" aria-label="City at night imagery"></div>
</section>

<!-- 12 funded -->
<section class="slide">
  <div class="photo ph-ice" style="left:0;top:0;width:389px;height:120px" role="img" aria-label="Digital portrait with binary code, blue tones"></div>
  <div class="abs num" style="left:150px;top:102px;width:24px;height:24px;border-radius:50%;background:var(--steel);line-height:24px">01</div>
  <div class="abs num" style="left:240px;top:20px;width:24px;height:24px;border-radius:50%;background:var(--teal);line-height:24px">02</div>
  <div class="abs num" style="left:330px;top:40px;width:24px;height:24px;border-radius:50%;background:var(--navy);line-height:24px">03</div>
  <div class="abs" style="left:14px;top:140px;width:170px;font:700 9px/1.35 'Raleway',sans-serif;color:var(--navy)">You've Funded Your Growth The Hard Way. By Selling Real Value To Real Customers.</div>
  <div class="p abs" style="left:200px;top:136px;width:175px">Short supporting copy for this statement. Add a few lines on how the firm helps teams grow faster with patient capital and hands-on support.</div>
</section>

<!-- 13 differences -->
<section class="slide std">
  <div class="title">Our Differences</div><div class="brand">Arvelle</div>
  <div class="panel" style="left:14px;top:42px;width:200px;height:160px;background:var(--steel)"></div>
  <div class="ic sky" style="left:24px;top:56px"></div><div class="p w abs" style="left:42px;top:56px;width:160px">Point one about what sets the firm apart.</div>
  <div class="ic sky" style="left:24px;top:90px"></div><div class="p w abs" style="left:42px;top:90px;width:160px">Point two about what sets the firm apart.</div>
  <div class="ic sky" style="left:24px;top:124px"></div><div class="p w abs" style="left:42px;top:124px;width:160px">Point three about what sets the firm apart.</div>
  <div class="ic sky" style="left:24px;top:158px"></div><div class="p w abs" style="left:42px;top:158px;width:160px">Point four about what sets the firm apart.</div>
  <div class="photo ph-ice" style="left:220px;top:42px;width:158px;height:160px" role="img" aria-label="Modern office escalators"></div>
</section>

<!-- 14 two column -->
<section class="slide std">
  <div class="title">Two Column Description</div><div class="brand">Arvelle</div>
  <div class="lead abs" style="left:14px;top:44px;width:300px">This is place for your header text. Insert your text here, just replace this text with your own text.</div>
  <div class="p abs" style="left:14px;top:78px;width:170px">Column one copy. Describe the first idea in a few short lines so it reads well at a glance.<br><br>Add a second paragraph with one more plain detail for the audience.</div>
  <div class="p abs" style="left:200px;top:78px;width:170px">Column two copy. Describe the second idea in a few short lines so it reads well at a glance.<br><br>Add a second paragraph with one more plain detail for the audience.</div>
</section>

<!-- 15 coffee break -->
<section class="slide">
  <div class="photo ph-teal" style="inset:0" role="img" aria-label="Soft teal gradient background"></div>
  <div class="brand" style="top:10px">Arvelle</div>
  <div class="ic" style="left:30px;top:106px;background:#fff;width:10px;height:10px"></div>
  <div class="cap abs" style="left:30px;top:124px;font-size:9px">COFFEE BREAK</div>
  <div class="p w abs" style="left:30px;top:136px">Short pause</div>
</section>

<!-- 16 three column -->
<section class="slide std">
  <div class="title">Three Column Description</div><div class="brand">Arvelle</div>
  <div class="lead abs" style="left:14px;top:44px;width:300px">This is place for your header text. Insert your text here, just replace this text with your own text.</div>
  <div class="p abs" style="left:14px;top:80px;width:112px">First column copy with a few short lines on the topic.<br><br>One more detail for this column.</div>
  <div class="p abs" style="left:138px;top:80px;width:112px">Second column copy with a few short lines on the topic.<br><br>One more detail for this column.</div>
  <div class="p abs" style="left:262px;top:80px;width:112px">Third column copy with a few short lines on the topic.<br><br>One more detail for this column.</div>
</section>

<!-- 17 photo + panel -->
<section class="slide">
  <div class="photo ph-dark" style="inset:0" role="img" aria-label="Blue light streaks in a data tunnel"></div>
  <div class="panel" style="left:262px;top:0;width:127px;height:215px;background:var(--steel);opacity:.92"></div>
  <div class="brand light" style="left:274px;right:auto;top:22px;font-size:16px">Arvelle</div>
  <div class="abs" style="left:274px;top:62px;width:100px;font:700 12px/1.25 'Raleway',sans-serif;color:#fff">Your Title Goes Here</div>
  <div class="ic" style="left:276px;top:110px;background:#fff"></div>
  <div class="ic" style="left:300px;top:110px;background:#fff"></div>
  <div class="ic" style="left:324px;top:110px;background:#fff"></div>
  <div class="p w abs" style="left:274px;top:190px">yourwebsite.example</div>
</section>

<!-- 18 numbered -->
<section class="slide std">
  <div class="title">Your Title Goes Here</div><div class="brand">Arvelle</div>
  <div class="h abs" style="left:14px;top:40px">Heading Goes Here</div>
  <div class="ic teal" style="left:16px;top:60px"></div><div class="abs" style="left:34px;top:60px;width:140px"><div class="h">Your Text Here</div><div class="p">Brief detail on this step.</div></div>
  <div class="ic" style="left:16px;top:100px"></div><div class="abs" style="left:34px;top:100px;width:140px"><div class="h">Your Text Here</div><div class="p">Brief detail on this step.</div></div>
  <div class="ic" style="left:16px;top:140px;background:var(--gray)"></div><div class="abs" style="left:34px;top:140px;width:140px"><div class="h">Your Text Here</div><div class="p">Brief detail on this step.</div></div>
  <div class="bar num" style="left:190px;top:52px;width:20px;height:28px;line-height:28px;background:var(--steel)">1</div><div class="panel" style="left:212px;top:52px;width:166px;height:28px;background:var(--steel)"><div class="p w" style="padding:5px 8px">Short note on step one of the plan.</div></div>
  <div class="bar num" style="left:190px;top:94px;width:20px;height:28px;line-height:28px;background:var(--teal)">2</div><div class="panel" style="left:212px;top:94px;width:166px;height:28px;background:var(--teal)"><div class="p w" style="padding:5px 8px">Short note on step two of the plan.</div></div>
  <div class="bar num" style="left:190px;top:136px;width:20px;height:28px;line-height:28px;background:var(--gray)">3</div><div class="panel" style="left:212px;top:136px;width:166px;height:28px;background:var(--gray)"><div class="p w" style="padding:5px 8px">Short note on step three of the plan.</div></div>
</section>

<!-- 19 four bullets -->
<section class="slide std">
  <div class="title">Four Bullets with Paragraph</div><div class="brand">Arvelle</div>
  <div class="ic" style="left:16px;top:52px"></div><div class="abs" style="left:32px;top:52px;width:70px"><div class="h">Your Text Here</div><div class="p">Brief detail</div></div>
  <div class="ic" style="left:106px;top:52px"></div><div class="abs" style="left:122px;top:52px;width:70px"><div class="h">Your Text Here</div><div class="p">Brief detail</div></div>
  <div class="ic" style="left:16px;top:120px"></div><div class="abs" style="left:32px;top:120px;width:70px"><div class="h">Your Text Here</div><div class="p">Brief detail</div></div>
  <div class="ic" style="left:106px;top:120px"></div><div class="abs" style="left:122px;top:120px;width:70px"><div class="h">Your Text Here</div><div class="p">Brief detail</div></div>
  <div class="abs" style="left:210px;top:48px;width:165px"><div class="h">Heading Goes Here</div><div class="p" style="margin-top:4px">Short paragraph that explains the four points in plain words.</div><div class="p" style="margin-top:6px">● One more note on the first point.</div><div class="p" style="margin-top:4px">● One more note on the second point.</div></div>
</section>

<!-- 20 your title photo middle -->
<section class="slide std">
  <div class="title">Your Title</div><div class="brand">Arvelle</div>
  <div class="abs" style="left:14px;top:44px;width:118px"><div class="h">Heading Goes Here</div><div class="p" style="margin-top:4px">Short copy for this slide in a few lines so it reads clearly.</div><div class="p" style="margin-top:6px">One more plain detail here.</div></div>
  <div class="photo ph-ice" style="left:140px;top:34px;width:100px;height:170px" role="img" aria-label="Glass office building interior"></div>
  <div class="ic" style="left:252px;top:52px"></div><div class="abs" style="left:268px;top:52px"><div class="h">Your Text Here</div><div class="p">Brief detail</div></div>
  <div class="ic" style="left:252px;top:88px"></div><div class="abs" style="left:268px;top:88px"><div class="h">Your Text Here</div><div class="p">Brief detail</div></div>
  <div class="ic" style="left:252px;top:124px"></div><div class="abs" style="left:268px;top:124px"><div class="h">Your Text Here</div><div class="p">Brief detail</div></div>
  <div class="ic" style="left:252px;top:160px"></div><div class="abs" style="left:268px;top:160px"><div class="h">Your Text Here</div><div class="p">Brief detail</div></div>
</section>

<!-- 21 text & bullet -->
<section class="slide std">
  <div class="title">Text &amp; Bullet Area</div><div class="brand">Arvelle</div>
  <div class="abs" style="left:14px;top:44px;width:120px"><div class="h">Heading Goes Here</div><div class="p" style="margin-top:4px">Short copy for this slide in a few lines so it reads clearly and fits the space.</div><div class="p" style="margin-top:6px">One more plain detail here.</div></div>
  <div class="ic teal" style="left:150px;top:48px"></div><div class="abs" style="left:166px;top:48px"><div class="h">Your Text Here</div><div class="p">Brief detail</div></div>
  <div class="ic teal" style="left:150px;top:86px"></div><div class="abs" style="left:166px;top:86px"><div class="h">Your Text Here</div><div class="p">Brief detail</div></div>
  <div class="ic teal" style="left:150px;top:124px"></div><div class="abs" style="left:166px;top:124px"><div class="h">Your Text Here</div><div class="p">Brief detail</div></div>
  <div class="ic teal" style="left:150px;top:162px"></div><div class="abs" style="left:166px;top:162px"><div class="h">Your Text Here</div><div class="p">Brief detail</div></div>
  <div class="ic" style="left:268px;top:48px"></div><div class="abs" style="left:284px;top:48px"><div class="h">Your Text Here</div><div class="p">Brief detail</div></div>
  <div class="ic" style="left:268px;top:86px"></div><div class="abs" style="left:284px;top:86px"><div class="h">Your Text Here</div><div class="p">Brief detail</div></div>
  <div class="ic" style="left:268px;top:124px"></div><div class="abs" style="left:284px;top:124px"><div class="h">Your Text Here</div><div class="p">Brief detail</div></div>
  <div class="ic" style="left:268px;top:162px"></div><div class="abs" style="left:284px;top:162px"><div class="h">Your Text Here</div><div class="p">Brief detail</div></div>
</section>

<!-- 22 section title -->
<section class="slide">
  <div class="photo ph-sky" style="inset:0" role="img" aria-label="Steel bridge structure with blue tint"></div>
  <div class="brand" style="top:14px;font-size:16px">Arvelle</div>
  <div class="p w abs" style="left:60px;top:112px">Section</div>
  <div class="abs" style="left:14px;top:124px;font:700 12px 'Raleway',sans-serif;color:#fff">Your Title Goes Here</div>
  <div class="p w abs" style="left:40px;top:142px">Your subtitle here</div>
</section>

<!-- 23 paragraph three bullet -->
<section class="slide std">
  <div class="title">Paragraph with Three Bullet</div><div class="brand">Arvelle</div>
  <div class="lead abs" style="left:14px;top:44px;width:300px">This is place for your header text. Insert your text here, just replace this text with your own text.</div>
  <div class="p abs" style="left:14px;top:80px;width:120px">Short copy for this slide in a few lines.<br><br>One more plain detail for the audience here.</div>
  <div class="ic" style="left:178px;top:84px"></div><div class="abs" style="left:150px;top:102px;width:70px;text-align:center"><div class="h">Your Text Here</div><div class="p">Brief detail on point.</div></div>
  <div class="ic" style="left:254px;top:84px"></div><div class="abs" style="left:226px;top:102px;width:70px;text-align:center"><div class="h">Your Text Here</div><div class="p">Brief detail on point.</div></div>
  <div class="ic" style="left:330px;top:84px"></div><div class="abs" style="left:302px;top:102px;width:70px;text-align:center"><div class="h">Your Text Here</div><div class="p">Brief detail on point.</div></div>
</section>

<!-- 24 global world -->
<section class="slide std">
  <div class="title">Global Experience</div><div class="brand">Arvelle</div>
  <div class="photo ph-map" style="left:24px;top:40px;width:340px;height:130px;border-radius:30px" role="img" aria-label="Gray world map with office locations"></div>
  <div class="pin" style="left:80px;top:78px"></div>
  <div class="pin" style="left:110px;top:120px"></div>
  <div class="pin" style="left:196px;top:66px"></div>
  <div class="pin" style="left:214px;top:96px"></div>
  <div class="pin" style="left:268px;top:82px"></div>
  <div class="pin" style="left:318px;top:132px"></div>
  <div class="abs" style="left:16px;top:176px"><div class="h">■ Heading Goes Here</div><div class="p">Short note on the offices shown.</div></div>
</section>

<!-- 25 global US -->
<section class="slide std">
  <div class="title">Global Experience</div><div class="brand">Arvelle</div>
  <div class="photo ph-map" style="left:14px;top:44px;width:240px;height:150px;border-radius:10px" role="img" aria-label="United States map with highlighted states"></div>
  <div class="panel" style="left:96px;top:120px;width:40px;height:34px;border-radius:6px;background:var(--steel);opacity:.8"></div>
  <div class="panel" style="left:150px;top:96px;width:30px;height:28px;border-radius:6px;background:var(--teal);opacity:.85"></div>
  <div class="panel" style="left:60px;top:90px;width:24px;height:24px;border-radius:6px;background:var(--slate);opacity:.8"></div>
  <div class="abs" style="left:268px;top:130px;width:110px"><div class="h">Content Title</div><div class="p">Short note on the regions highlighted here.</div></div>
</section>

<!-- 26 multiple column -->
<section class="slide std">
  <div class="title">Multiple Column Area</div><div class="brand">Arvelle</div>
  <div class="ic teal" style="left:34px;top:50px"></div><div class="ic teal" style="left:104px;top:50px"></div><div class="ic teal" style="left:174px;top:50px"></div><div class="ic teal" style="left:244px;top:50px"></div><div class="ic teal" style="left:314px;top:50px"></div>
  <div class="abs h" style="left:14px;top:70px;width:360px;display:flex;justify-content:space-between"><span>Your Text</span><span>Your Text</span><span>Your Text</span><span>Your Text</span><span>Your Text</span></div>
  <div class="abs" style="left:14px;top:118px;width:170px"><div class="h">Heading Goes Point</div><div class="p">Short copy for this column in a few plain lines for the reader.</div></div>
  <div class="abs" style="left:200px;top:118px;width:170px"><div class="h">Heading Goes Point</div><div class="p">Short copy for this column in a few plain lines for the reader.</div></div>
</section>

<!-- 27 pie rings -->
<section class="slide std">
  <div class="title">Your Pie Chart Area</div><div class="brand">Arvelle</div>
  <svg class="abs" style="left:14px;top:42px" width="360" height="60" viewBox="0 0 360 60">
    <g fill="none" stroke-width="5" transform="rotate(-90)">
      <circle cx="-30" cy="45" r="20" stroke="#e3eaee"/><circle cx="-30" cy="45" r="20" stroke="#5f97b5" stroke-dasharray="25 126"/>
      <circle cx="-30" cy="135" r="20" stroke="#e3eaee"/><circle cx="-30" cy="135" r="20" stroke="#5f97b5" stroke-dasharray="50 126"/>
      <circle cx="-30" cy="225" r="20" stroke="#e3eaee"/><circle cx="-30" cy="225" r="20" stroke="#85cae6" stroke-dasharray="75 126"/>
      <circle cx="-30" cy="315" r="20" stroke="#e3eaee"/><circle cx="-30" cy="315" r="20" stroke="#1b3657" stroke-dasharray="101 126"/>
    </g>
    <g font-family="Raleway,sans-serif" font-size="8" font-weight="700" fill="#1b3657" text-anchor="middle">
      <text x="45" y="33">20%</text><text x="135" y="33">40%</text><text x="225" y="33">60%</text><text x="315" y="33">80%</text>
    </g>
  </svg>
  <div class="abs" style="left:14px;top:112px;width:360px;display:flex;justify-content:space-between;text-align:center">
    <div style="width:80px"><div class="h">Title Text Here</div><div class="p">Brief detail on this share.</div></div>
    <div style="width:80px"><div class="h">Title Text Here</div><div class="p">Brief detail on this share.</div></div>
    <div style="width:80px"><div class="h">Title Text Here</div><div class="p">Brief detail on this share.</div></div>
    <div style="width:80px"><div class="h">Title Text Here</div><div class="p">Brief detail on this share.</div></div>
  </div>
</section>

<!-- 28 donut -->
<section class="slide std">
  <div class="title">Your Pie Chart Area</div><div class="brand">Arvelle</div>
  <svg class="abs" style="left:150px;top:56px" width="90" height="90" viewBox="0 0 90 90">
    <g fill="none" stroke-width="16" transform="rotate(-90 45 45)">
      <circle cx="45" cy="45" r="32" stroke="#1b3657" stroke-dasharray="70 201"/>
      <circle cx="45" cy="45" r="32" stroke="#5f97b5" stroke-dasharray="55 201" stroke-dashoffset="-70"/>
      <circle cx="45" cy="45" r="32" stroke="#85cae6" stroke-dasharray="40 201" stroke-dashoffset="-125"/>
      <circle cx="45" cy="45" r="32" stroke="#c8d2da" stroke-dasharray="36 201" stroke-dashoffset="-165"/>
    </g>
  </svg>
  <div class="ic" style="left:110px;top:58px"></div><div class="abs" style="left:30px;top:56px;width:76px;text-align:right"><div class="h">Title Here</div><div class="p">Brief detail</div></div>
  <div class="ic sky" style="left:110px;top:128px"></div><div class="abs" style="left:30px;top:126px;width:76px;text-align:right"><div class="h">Title Here</div><div class="p">Brief detail</div></div>
  <div class="ic" style="left:266px;top:58px;background:var(--navy)"></div><div class="abs" style="left:284px;top:56px;width:90px"><div class="h">Title Here</div><div class="p">Brief detail</div></div>
  <div class="ic" style="left:266px;top:128px;background:var(--gray)"></div><div class="abs" style="left:284px;top:126px;width:90px"><div class="h">Title Here</div><div class="p">Brief detail</div></div>
  <div class="p abs" style="left:60px;top:180px;width:270px;text-align:center">Short caption explaining the split shown in the chart above.</div>
</section>

<!-- 29 pie -->
<section class="slide std">
  <div class="title">Your Pie Chart Area</div><div class="brand">Arvelle</div>
  <svg class="abs" style="left:40px;top:48px" width="120" height="96" viewBox="0 0 120 96">
    <ellipse cx="60" cy="52" rx="55" ry="38" fill="#8fa2b2"/>
    <ellipse cx="60" cy="45" rx="55" ry="38" fill="#c8d2da"/>
    <path d="M60 45 L60 7 A55 38 0 0 1 113 55 Z" fill="#5f97b5"/>
    <path d="M60 45 L113 55 A55 38 0 0 1 40 81 Z" fill="#85cae6"/>
  </svg>
  <div class="abs" style="left:16px;top:160px;font:800 16px 'Raleway',sans-serif;color:var(--steel)">54%</div>
  <div class="abs" style="left:64px;top:160px;width:300px"><div class="h">Heading Goes Here</div><div class="p">Short caption explaining the main share in this chart.</div></div>
  <div class="ic" style="left:220px;top:60px"></div><div class="abs" style="left:238px;top:60px"><div class="h">Your Text Here</div><div class="p">Brief detail</div></div>
  <div class="ic sky" style="left:220px;top:90px"></div><div class="abs" style="left:238px;top:90px"><div class="h">Your Text Here</div><div class="p">Brief detail</div></div>
  <div class="ic" style="left:220px;top:120px;background:var(--pale)"></div><div class="abs" style="left:238px;top:120px"><div class="h">Your Text Here</div><div class="p">Brief detail</div></div>
</section>

<!-- 30 divider green -->
<section class="slide">
  <div class="photo ph-green" style="inset:0" role="img" aria-label="Green falling code background"></div>
  <div class="panel" style="left:180px;top:0;width:209px;height:215px;background:#fff;clip-path:polygon(40% 0,100% 0,100% 100%,0 100%)"></div>
  <div class="brand" style="top:120px;font-size:14px">Arvelle</div>
  <div class="abs" style="right:14px;top:140px;font:700 10px 'Raleway',sans-serif;color:var(--navy)">Divider Page</div>
  <div class="p abs" style="right:14px;top:154px">Your Subtitle here</div>
</section>

<!-- 31 divider blue -->
<section class="slide">
  <div class="photo ph-sky" style="left:0;top:0;width:389px;height:215px" role="img" aria-label="Blue binary pattern background"></div>
  <div class="panel" style="left:0;top:0;width:230px;height:215px;background:#fff;clip-path:polygon(0 0,60% 0,100% 50%,60% 100%,0 100%)"></div>
  <div class="brand" style="left:60px;right:auto;top:120px;font-size:14px">Arvelle</div>
  <div class="abs" style="left:60px;top:140px;font:700 10px 'Raleway',sans-serif;color:var(--navy)">Divider Page</div>
  <div class="p abs" style="left:60px;top:154px">Your Subtitle here</div>
</section>

<!-- 32 statement dark -->
<section class="slide">
  <div class="photo ph-dark" style="inset:0" role="img" aria-label="Dark blue abstract light rays"></div>
  <div class="panel" style="left:120px;top:0;width:180px;height:215px;background:rgba(133,202,230,.18);clip-path:polygon(40% 0,100% 0,60% 100%,0 100%)"></div>
  <div class="abs" style="left:200px;top:70px;width:160px;text-align:right;font:400 12px/1.3 'Raleway',sans-serif;color:#fff">You Need a <b>Different Kind Of</b> Capital</div>
</section>

<!-- 33 population -->
<section class="slide std">
  <div class="title">Population Chart</div><div class="brand">Arvelle</div>
  <div class="photo ph-map" style="left:14px;top:44px;width:200px;height:110px;border-radius:20px" role="img" aria-label="Gray world map"></div>
  <div class="pin" style="left:60px;top:80px"></div>
  <div class="pin teal" style="left:120px;top:70px"></div>
  <div class="pin" style="left:170px;top:110px"></div>
  <svg class="abs" style="left:230px;top:64px" width="150" height="64" viewBox="0 0 150 64">
    <g fill="none" stroke-width="4" transform="rotate(-90 32 32)"><circle cx="32" cy="32" r="26" stroke="#e3eaee"/><circle cx="32" cy="32" r="26" stroke="#5f97b5" stroke-dasharray="73 163"/></g>
    <g fill="none" stroke-width="4" transform="rotate(-90 115 32)"><circle cx="115" cy="32" r="26" stroke="#e3eaee"/><circle cx="115" cy="32" r="26" stroke="#1b3657" stroke-dasharray="90 163"/></g>
    <g font-family="Raleway,sans-serif" font-size="10" font-weight="700" text-anchor="middle"><text x="32" y="36" fill="#5f97b5">45%</text><text x="115" y="36" fill="#1b3657">55%</text></g>
  </svg>
  <div class="p abs" style="left:14px;top:166px;width:200px">Short caption about the population figures shown on the map.</div>
  <div class="abs h" style="left:246px;top:140px;width:130px;display:flex;justify-content:space-between"><span>1,200,000</span><span>1,450,000</span></div>
</section>

<!-- 34 market performance -->
<section class="slide std">
  <div class="title">Market Performance</div><div class="brand">Arvelle</div>
  <svg class="abs" style="left:14px;top:44px" width="220" height="160" viewBox="0 0 220 160">
    <g fill="#c8d2da">
      <rect x="30" y="2" width="180" height="18"/><rect x="30" y="36" width="180" height="18"/><rect x="30" y="70" width="180" height="18"/><rect x="30" y="104" width="180" height="18"/><rect x="30" y="138" width="180" height="18"/>
    </g>
    <g fill="#5f97b5"><rect x="30" y="2" width="80" height="18"/><rect x="30" y="36" width="60" height="18"/><rect x="30" y="70" width="40" height="18"/><rect x="30" y="104" width="30" height="18"/><rect x="30" y="138" width="20" height="18"/></g>
    <g fill="#1b3657"><circle cx="11" cy="11" r="10"/><circle cx="11" cy="45" r="10"/><circle cx="11" cy="79" r="10"/><circle cx="11" cy="113" r="10"/><circle cx="11" cy="147" r="10"/></g>
    <g stroke="#fff" stroke-width="2" fill="none"><path d="M120 5 l6 6 -6 6 M135 5 l6 6 -6 6 M150 5 l6 6 -6 6 M165 5 l6 6 -6 6 M180 5 l6 6 -6 6"/></g>
  </svg>
  <div class="abs" style="left:250px;top:44px;width:130px"><div class="h">Finance</div><div class="p">Brief note on this market.</div><div class="h" style="margin-top:6px">System</div><div class="p">Brief note on this market.</div><div class="h" style="margin-top:6px">Market</div><div class="p">Brief note on this market.</div><div class="h" style="margin-top:6px">Data model</div><div class="p">Brief note on this market.</div></div>
</section>

<!-- 35 european map -->
<section class="slide std">
  <div class="title">European Map Analisys</div><div class="brand">Arvelle</div>
  <div class="abs" style="left:14px;top:44px;width:160px"><div class="h">Heading Goes Here</div><div class="p">Short copy on the regional split shown on the map here.</div></div>
  <div class="abs" style="left:14px;top:96px;font:800 13px 'Raleway',sans-serif;color:var(--steel)">45%</div><div class="abs" style="left:70px;top:96px;font:800 13px 'Raleway',sans-serif;color:var(--teal)">864,954</div>
  <div class="abs" style="left:14px;top:130px;font:800 13px 'Raleway',sans-serif;color:var(--steel)">65%</div><div class="abs" style="left:70px;top:130px;font:800 13px 'Raleway',sans-serif;color:var(--teal)">356,451</div>
  <div class="photo ph-map" style="left:220px;top:60px;width:160px;height:140px;border-radius:16px" role="img" aria-label="Gray map of Europe"></div>
  <div class="pin" style="left:262px;top:96px"></div>
  <div class="pin teal" style="left:330px;top:140px"></div>
  <div class="panel" style="left:240px;top:40px;width:80px;height:12px;background:var(--steel)"><div class="p w" style="line-height:12px;padding-left:5px">Region One</div></div>
  <div class="panel" style="left:300px;top:170px;width:70px;height:12px;background:var(--teal)"><div class="p w" style="line-height:12px;padding-left:5px">Region Two</div></div>
</section>

<!-- 36 performance level -->
<section class="slide std">
  <div class="title">Performance Level</div><div class="brand">Arvelle</div>
  <svg class="abs" style="left:145px;top:48px" width="100" height="100" viewBox="0 0 100 100">
    <g fill="none" stroke-width="18" transform="rotate(-90 50 50)">
      <circle cx="50" cy="50" r="36" stroke="#5f97b5" stroke-dasharray="54 226"/>
      <circle cx="50" cy="50" r="36" stroke="#86cfc6" stroke-dasharray="54 226" stroke-dashoffset="-57"/>
      <circle cx="50" cy="50" r="36" stroke="#1b3657" stroke-dasharray="54 226" stroke-dashoffset="-114"/>
      <circle cx="50" cy="50" r="36" stroke="#85cae6" stroke-dasharray="54 226" stroke-dashoffset="-171"/>
    </g>
    <g font-family="Raleway,sans-serif" font-size="7" font-weight="700" fill="#fff" text-anchor="middle"><text x="75" y="30">01</text><text x="75" y="76">02</text><text x="27" y="76">03</text><text x="27" y="30">04</text></g>
  </svg>
  <div class="abs" style="left:20px;top:56px;width:110px;text-align:right"><div class="h">Global</div><div class="p">Brief detail on this level.</div></div>
  <div class="abs" style="left:20px;top:116px;width:110px;text-align:right"><div class="h">Market</div><div class="p">Brief detail on this level.</div></div>
  <div class="abs" style="left:262px;top:56px;width:110px"><div class="h">Finance</div><div class="p">Brief detail on this level.</div></div>
  <div class="abs" style="left:262px;top:116px;width:110px"><div class="h">Growth</div><div class="p">Brief detail on this level.</div></div>
  <div class="p abs" style="left:40px;top:174px;width:310px;text-align:center">Short caption on how the four levels work together over time.</div>
</section>

<!-- 37 master option -->
<section class="slide">
  <div class="panel" style="left:0;top:0;width:389px;height:28px;background:var(--navy)"></div>
  <div class="title" style="color:#fff;top:8px">Other Option of Master Slide</div><div class="brand light" style="top:7px">Arvelle</div>
  <div class="p abs" style="left:14px;bottom:6px">yourwebsite.example</div>
</section>

<!-- 38 photo boxes -->
<section class="slide">
  <div class="photo ph-dark" style="inset:0" role="img" aria-label="Blue data light background"></div>
  <div class="panel" style="left:0;top:0;width:150px;height:62px;background:var(--deep)"><div class="p w" style="padding:8px 12px">Short copy describing the slide topic in a few plain lines.</div></div>
  <div class="panel" style="left:0;top:118px;width:110px;height:40px;background:var(--steel)"><div class="p w" style="padding:6px 10px">Brief note here.</div></div>
  <div class="panel" style="left:0;top:160px;width:110px;height:40px;background:var(--teal)"><div class="p w" style="padding:6px 10px">Brief note here.</div></div>
  <div class="panel" style="left:200px;top:72px;width:90px;height:34px;background:var(--teal)"></div>
  <div class="panel" style="left:290px;top:72px;width:99px;height:34px;background:var(--steel)"></div>
  <div class="panel" style="left:200px;top:106px;width:90px;height:34px;background:var(--steel)"></div>
  <div class="panel" style="left:290px;top:106px;width:99px;height:34px;background:var(--slate)"></div>
</section>

<!-- 39 mockup -->
<section class="slide">
  <div class="panel" style="left:0;top:0;width:389px;height:32px;background:var(--deep)"></div>
  <div class="cap abs" style="left:14px;top:12px;font-size:9px">OUR MOCKUP</div>
  <div class="h abs" style="left:14px;top:44px">Heading Here</div>
  <div class="ic" style="left:16px;top:70px"></div><div class="p abs" style="left:34px;top:70px;width:140px">Brief detail on this feature.</div>
  <div class="ic" style="left:16px;top:102px"></div><div class="p abs" style="left:34px;top:102px;width:140px">Brief detail on this feature.</div>
  <div class="ic" style="left:16px;top:134px"></div><div class="p abs" style="left:34px;top:134px;width:140px">Brief detail on this feature.</div>
  <div class="ic" style="left:16px;top:166px"></div><div class="p abs" style="left:34px;top:166px;width:140px">Brief detail on this feature.</div>
  <div class="photo" style="left:210px;top:40px;width:170px;height:130px;background:radial-gradient(circle at 50% 45%,#fff,#f1f4f6 45%,#cdd6dd)" role="img" aria-label="Desktop monitor mockup showing the deck"></div>
  <div class="brand" style="left:250px;right:auto;top:96px;font-size:20px">Arvelle</div>
</section>

<!-- 40 line chart -->
<section class="slide std">
  <div class="brand">Arvelle</div>
  <div class="abs" style="left:14px;top:82px;font:700 11px/1.3 'Raleway',sans-serif;color:var(--navy)">This Is Line<br>Chart Slide</div>
  <div class="panel" style="left:14px;top:118px;width:70px;height:10px;background:var(--sky)"></div>
  <div class="p abs" style="left:14px;top:134px;width:100px">Short note on the trend.</div>
  <svg class="abs" style="left:140px;top:50px" width="230" height="140" viewBox="0 0 230 140">
    <path d="M10 5 V120 H225" stroke="#c8d2da" fill="none"/>
    <path d="M20 90 L80 30 L140 100 L210 20" stroke="#1b3657" stroke-width="1.5" fill="none"/>
    <path d="M20 40 L80 70 L140 30 L210 90" stroke="#1b3657" stroke-width="1.5" fill="none"/>
    <g font-family="Open Sans,sans-serif" font-size="6" fill="#8a96a3"><text x="20" y="132">Item 1</text><text x="80" y="132">Item 2</text><text x="140" y="132">Item 3</text><text x="200" y="132">Item 4</text></g>
  </svg>
</section>

<!-- 41 brand detailed -->
<section class="slide std">
  <div class="title">Brand Detailed</div><div class="brand">Arvelle</div>
  <div class="photo" style="left:14px;top:40px;width:170px;height:164px;background:radial-gradient(circle at 50% 40%,#bfe6cf,transparent 60%),linear-gradient(180deg,#e8f5ec,#9fd3b3)" role="img" aria-label="Green falling code on light background"></div>
  <div class="panel" style="left:196px;top:60px;width:88px;height:60px;background:var(--steel)"><div style="padding:6px"><div class="h w">System</div><div class="p w">Brief note here.</div></div></div>
  <div class="panel" style="left:288px;top:60px;width:88px;height:60px;background:var(--slate)"><div style="padding:6px"><div class="h w">Market</div><div class="p w">Brief note here.</div></div></div>
  <div class="panel" style="left:196px;top:124px;width:88px;height:60px;background:var(--teal)"><div style="padding:6px"><div class="h w">Finance</div><div class="p w">Brief note here.</div></div></div>
  <div class="panel" style="left:288px;top:124px;width:88px;height:60px;background:var(--steel)"><div style="padding:6px"><div class="h w">Growth</div><div class="p w">Brief note here.</div></div></div>
</section>

<!-- 42 title and image -->
<section class="slide std">
  <div class="title">Title And Image + Text</div><div class="brand">Arvelle</div>
  <div class="photo ph-dark" style="left:14px;top:38px;width:362px;height:88px" role="img" aria-label="Blue digital globe imagery"></div>
  <div class="abs" style="left:14px;top:136px;width:170px;font:700 8px/1.35 'Raleway',sans-serif;color:var(--navy)">Short headline text for this image slide set over two or three lines here.</div>
  <div class="p abs" style="left:200px;top:136px;width:175px">Body copy describing the image and the point it makes for investors in a few plain lines.</div>
</section>

<!-- 43 three bullets -->
<section class="slide std">
  <div class="title">Three Bullets Area</div><div class="brand">Arvelle</div>
  <div class="photo ph-dark" style="left:0;top:96px;width:389px;height:119px" role="img" aria-label="Blue city horizon at dusk"></div>
  <div class="abs" style="left:60px;top:168px;width:30px;height:30px;border-radius:50%;background:var(--steel)"></div>
  <div class="abs" style="left:180px;top:168px;width:30px;height:30px;border-radius:50%;background:var(--teal)"></div>
  <div class="abs" style="left:300px;top:168px;width:30px;height:30px;border-radius:50%;background:var(--slate)"></div>
  <div class="p abs" style="left:14px;top:44px;width:360px">Short copy introducing the three points shown below in plain words.</div>
</section>

<!-- 44 team -->
<section class="slide std">
  <div class="title">Our Team</div><div class="brand">Arvelle</div>
  <div class="photo ph-ice" style="left:14px;top:46px;width:66px;height:70px" role="img" aria-label="Team member portrait"></div>
  <div class="photo ph-ice" style="left:88px;top:46px;width:66px;height:70px" role="img" aria-label="Team member portrait"></div>
  <div class="photo ph-ice" style="left:162px;top:46px;width:66px;height:70px" role="img" aria-label="Team member portrait"></div>
  <div class="photo ph-ice" style="left:236px;top:46px;width:66px;height:70px" role="img" aria-label="Team member portrait"></div>
  <div class="photo ph-ice" style="left:310px;top:46px;width:66px;height:70px" role="img" aria-label="Team member portrait"></div>
  <div class="panel" style="left:14px;top:116px;width:66px;height:12px;background:var(--steel)"><div class="p w" style="text-align:center;line-height:12px">Mara Lind</div></div>
  <div class="panel" style="left:88px;top:116px;width:66px;height:12px;background:var(--steel)"><div class="p w" style="text-align:center;line-height:12px">Owen Hale</div></div>
  <div class="panel" style="left:162px;top:116px;width:66px;height:12px;background:var(--steel)"><div class="p w" style="text-align:center;line-height:12px">Ivo Brandt</div></div>
  <div class="panel" style="left:236px;top:116px;width:66px;height:12px;background:var(--steel)"><div class="p w" style="text-align:center;line-height:12px">Lena Voss</div></div>
  <div class="panel" style="left:310px;top:116px;width:66px;height:12px;background:var(--steel)"><div class="p w" style="text-align:center;line-height:12px">Tom Reyes</div></div>
  <div class="p abs" style="left:14px;top:134px;width:66px">Partner. Short bio line.</div>
  <div class="p abs" style="left:88px;top:134px;width:66px">Partner. Short bio line.</div>
  <div class="p abs" style="left:162px;top:134px;width:66px">Partner. Short bio line.</div>
  <div class="p abs" style="left:236px;top:134px;width:66px">Analyst. Short bio line.</div>
  <div class="p abs" style="left:310px;top:134px;width:66px">Analyst. Short bio line.</div>
</section>

<!-- 45 thank you -->
<section class="slide">
  <div class="photo" style="inset:0;background:radial-gradient(circle at 70% 40%,rgba(133,202,230,.35),transparent 45%),linear-gradient(135deg,#071529,#143a66 60%,#245c92)" role="img" aria-label="Dark blue data background"></div>
  <div class="panel" style="left:0;top:100px;width:300px;height:56px;background:var(--steel);clip-path:polygon(0 0,100% 0,85% 100%,0 100%)"></div>
  <div class="cap abs" style="left:40px;top:116px;font-size:10px">THANK YOU</div>
  <div class="p w abs" style="left:40px;top:132px">For Your Precious Time</div>
  <div class="brand light" style="top:112px;right:40px;font-size:22px">Arvelle</div>
</section>

</main>
</body>
</html>
```